New York IT Service, Technology & Security Co.

need a new business card design for our Technology & Security Company. We are a Computer Networking Company, Security Camera Installers, Phone Systems.

Target Market(s)

Construction, Medical, Law Offices, Accounting, Retail etc.

Industry/Entity Type

Information Technology

Contact Information for Business Card

Logo is attached, colors are Blue, Red, Black. Blue for Technology & Red is for Security Cameras, Access Control, Alarm Systems

Colors
fbed22
ec1f27
0555a3
ffffff

Requirements
Must have
• Pictures or Icons for
• For Technology:
• Computer, Network, Phone System, Copier, TV, Cabling
• For Security:
• Video Surveillance, Access Control, Intercom, Fire Alarm, Burglar Alarm, Time Clock

```html
<!DOCTYPE html>
<html lang="en">
<head>
<meta charset="utf-8">
<title>Hudson Tech Service – Business Card</title>
<link href="https://fonts.googleapis.com/css2?family=Open+Sans:wght@400;600;800&family=Didact+Gothic&display=swap" rel="stylesheet">
<style>
  :root {
    --brand-blue: #0f6db8;
    --brand-red: #ec1f27;
    --ink: #1b1b1b;
    --muted: #666666;
    --paper: #ffffff;
    --backdrop: #e4e6e8;
  }
  * { box-sizing: border-box; margin: 0; padding: 0; }
  html, body { width: 1200px; height: 1000px; overflow: hidden; }
  body {
    background: var(--backdrop);
    position: relative;
    font-family: "Open Sans", Arial, sans-serif;
  }
  .card {
    position: absolute;
    left: 240px;
    width: 697px;
    height: 397px;
    background: var(--paper);
    border-radius: 14px;
    overflow: hidden;
    box-shadow: 0 4px 10px rgba(0,0,0,0.18);
  }
  .card-front { top: 83px; }
  .card-back { top: 520px; }

  .brand-name {
    font-family: "Open Sans", Arial, sans-serif;
    font-weight: 800;
    color: var(--ink);
    letter-spacing: -0.3px;
    white-space: nowrap;
  }
  .card-front .brand-name {
    position: absolute; left: 33px; top: 58px; font-size: 21px;
  }
  .person-name {
    position: absolute; left: 33px; top: 142px;
    font-size: 21px; font-weight: 600; letter-spacing: 0.5px;
    color: var(--brand-blue);
  }
  .person-name .surname { color: var(--brand-red); }
  .person-role {
    position: absolute; left: 33px; top: 170px;
    font-size: 16px; color: var(--muted);
  }
  .address {
    position: absolute; left: 33px; top: 207px;
    font-size: 15.5px; line-height: 22px; color: var(--muted); font-style: normal;
  }
  .contact-list {
    position: absolute; left: 33px; top: 268px; list-style: none;
  }
  .contact-list li {
    display: flex; align-items: center; height: 22px;
    font-size: 15.5px; color: var(--muted);
  }
  .contact-list svg { width: 14px; height: 14px; margin-right: 15px; fill: var(--brand-blue); }
  .front-stripes { position: absolute; left: 0; bottom: 0; width: 697px; height: 34px; }

  .card-back .brand-name {
    position: absolute; left: 0; right: 0; top: 80px;
    text-align: center; font-size: 35px;
  }
  .service-row {
    position: absolute; left: 0; width: 697px; height: 76px;
    display: grid; grid-template-columns: repeat(6, 1fr); column-gap: 5px;
  }
  .service-row.technology { top: 200px; }
  .service-row.security { top: 299px; }
  .service-tile {
    display: flex; flex-direction: column; align-items: center; justify-content: center;
    color: var(--paper);
    font-family: "Didact Gothic", "Century Gothic", sans-serif;
    font-size: 16px; line-height: 19px; text-align: center; letter-spacing: 0.3px;
  }
  .technology .service-tile { background: var(--brand-blue); }
  .security .service-tile { background: var(--brand-red); }
  .service-tile svg {
    width: 22px; height: 22px; margin-bottom: 4px;
    fill: none; stroke: var(--paper); stroke-width: 1.6; stroke-linecap: round; stroke-linejoin: round;
  }
</style>
</head>
<body>

<section class="card card-front" aria-label="Card front">
  <div class="brand-name">HUDSON TECH SERVICE</div>
  <h1 class="person-name">DANIEL <span class="surname">BROOKS</span></h1>
  <p class="person-role">Founder</p>
  <address class="address">4870 Ridge Avenue,<br>Suite C204 Tucson 85711</address>
  <ul class="contact-list">
    <li><svg viewBox="0 0 14 14"><path d="M4 0h6a1 1 0 0 1 1 1v12a1 1 0 0 1-1 1H4a1 1 0 0 1-1-1V1a1 1 0 0 1 1-1zm.5 1.5v9h5v-9zM7 11.3a.8.8 0 1 0 0 1.6.8.8 0 0 0 0-1.6z"/></svg>800-555-0147</li>
    <li><svg viewBox="0 0 14 14"><path d="M0 3h14v1L7 8 0 4zM0 5.2l7 4 7-4V12H0z"/></svg>dbrooks@mailbox.com</li>
    <li><svg viewBox="0 0 14 14"><circle cx="7" cy="7" r="6.5"/><path d="M3 4c1 0 2 1 3 1s1 2 0 3-1 2 0 4M9 2c0 1-1 2 0 3s3 0 3 2" stroke="#fff" stroke-width="1" fill="none"/></svg>hudsontechservice.com</li>
  </ul>
  <svg class="front-stripes" viewBox="0 0 697 34" preserveAspectRatio="none" aria-hidden="true">
    <path d="M0 10 H395 Q405 10 400 14 H0 Z" fill="var(--brand-red)"/>
    <path d="M0 16 H398 Q412 16 425 8 Q440 0 470 0 H697 V34 H0 Z" fill="var(--brand-blue)"/>
    <path d="M0 22 H697 V34 H0 Z" fill="var(--brand-blue)"/>
  </svg>
</section>

<section class="card card-back" aria-label="Card back">
  <div class="brand-name">HUDSON TECH SERVICE</div>

  <div class="service-row technology">
    <div class="service-tile"><svg viewBox="0 0 22 22"><rect x="3" y="4" width="16" height="11" rx="1"/><path d="M8 19h6M11 15v4"/></svg>Computer</div>
    <div class="service-tile"><svg viewBox="0 0 22 22"><circle cx="11" cy="11" r="10"/><circle cx="7" cy="11" r="1.6"/><circle cx="14" cy="7" r="1.6"/><circle cx="14" cy="15" r="1.6"/><path d="M8.4 10.2l4.2-2.4M8.4 11.8l4.2 2.4"/></svg>Network</div>
    <div class="service-tile"><svg viewBox="0 0 22 22"><rect x="7" y="3" width="8" height="16" rx="1.5"/><path d="M10 16h2"/></svg>Phone System</div>
    <div class="service-tile"><svg viewBox="0 0 22 22"><path d="M5 9h12v8H5zM7 9V5h8v4M7 13h8M5 6h2"/></svg>Copier</div>
    <div class="service-tile"><svg viewBox="0 0 22 22"><rect x="3" y="4" width="16" height="11" rx="1"/><path d="M8 18h6"/></svg>TV</div>
    <div class="service-tile"><svg viewBox="0 0 22 22"><path d="M7 3v4M10 3v4M6 7h5v4H6zM8.5 11v4a3 3 0 0 0 6 0V8M14 4v4M12.5 8h3"/></svg>Cabling</div>
  </div>

  <div class="service-row security">
    <div class="service-tile"><svg viewBox="0 0 22 22"><path d="M3 7l12 3-1 4-12-3zM12 13l1 4h4M3 5v5"/></svg>Video<br>Surveillance</div>
    <div class="service-tile"><svg viewBox="0 0 22 22"><rect x="5" y="3" width="8" height="15" rx="1"/><path d="M7 6h4M7 9h1M10 9h1M7 12h1M10 12h1M15 8v10h3V8z"/></svg>Access<br>Control</div>
    <div class="service-tile"><svg viewBox="0 0 22 22"><rect x="6" y="3" width="10" height="16" rx="1"/><circle cx="11" cy="8" r="2"/><path d="M9 13h4M9 15h4"/></svg>Intercom</div>
    <div class="service-tile"><svg viewBox="0 0 22 22"><path d="M6 18v-6a5 5 0 0 1 10 0v6M4 18h14M11 2v3M4 5l2 2M18 5l-2 2"/></svg>Fire Alarm</div>
    <div class="service-tile"><svg viewBox="0 0 22 22"><circle cx="11" cy="11" r="2.2" fill="#fff"/><path d="M7 7a6 6 0 0 0 0 8M15 7a6 6 0 0 1 0 8M4.5 4.5a9.5 9.5 0 0 0 0 13M17.5 4.5a9.5 9.5 0 0 1 0 13"/></svg>Burglar<br>Alarm</div>
    <div class="service-tile"><svg viewBox="0 0 22 22"><circle cx="11" cy="11" r="9"/><path d="M11 6v5l3 2"/></svg>Time Clock</div>
  </div>
</section>

</body>
</html>
```